R.Morvane LLC Organizational Change and Development

I am starting my own company as a a senior facilitator, keynote speaker, executive coach, webinar training instructor, quality management adviser, and classroom presenter. I have taught diversity and cultural competence, organizational development, change management, leadership, organizational dynamics, team-building, accountability, negotiation, work-life balance, quality management, TRAK, and hundreds of web based trainings. I have a PhD. in Counseling Psychology, MBA, B.S. in Human Development, Family Studies, and a Master’s Practitioner of Neurolinguistic Programming. My degrees and certifications give me a foundation for advising a wide variety of people, industries, and cultures at all organizational levels. I would like a design that's fun, engaging, humorous, progressive, and has a professional feel. I really like the colors burgundy wine.

Target Market(s)

corporate America

Industry/Entity Type

Training

Number of Pages Required

5+ page

Colors
eb1f26
f04a50
3176b4
33a6d7

Requirements
Must have
• my different areas of expertise - fun visuals -easy for me to use
Should not have
• something that looks stiff, too traditional or boring

```html
<!DOCTYPE html>
<html lang="en">
<head>
<meta charset="utf-8">
<title>R. Morvane — Organizational Change and Development</title>
<link rel="stylesheet" href="https://fonts.googleapis.com/css2?family=Questrial&family=Libre+Caslon+Text&display=swap">
<style>
  :root {
    --coral: #f04a50;
    --red: #eb1f26;
    --blue: #2f73b3;
    --ink: #1f1f1f;
    --muted: #7a7a7a;
    --cream: #fdfcf6;
    --hero: #2b1a17;
    --footer: #f5f5f5;
    --rule: #e4e4e4;
  }
  * { box-sizing: border-box; margin: 0; padding: 0; }
  html, body { width: 1019px; height: 1200px; overflow: hidden; }
  body { position: relative; background: #fff; font-family: "Questrial", sans-serif; color: var(--ink); }

  .header-band { position: absolute; left: 0; top: 0; width: 1019px; height: 322px; background: var(--coral); }
  .cream-band { position: absolute; left: 0; top: 322px; width: 1019px; height: 38px; background: var(--cream); }

  .brand { position: absolute; left: 131px; top: 30px; font-family: "Libre Caslon Text", serif; font-size: 38px; color: #fff; letter-spacing: 0.5px; line-height: 1; }

  .main-nav { position: absolute; right: 127px; top: 40px; display: flex; }
  .main-nav a { color: #fff; text-decoration: none; font-size: 13.5px; padding: 8px 13px; border-left: 1px solid rgba(255,255,255,0.3); line-height: 1; }
  .main-nav a:first-child { border-left: none; }
  .main-nav a:last-child { padding-right: 0; }

  .hero { position: absolute; left: 124px; top: 102px; width: 771px; height: 380px; background: var(--hero); box-shadow: 0 2px 5px rgba(0,0,0,0.25); overflow: hidden; }
  .hero-photo { position: absolute; right: 0; top: 0; width: 420px; height: 380px;
    background: radial-gradient(ellipse at 62% 35%, #6a4a36 0%, #4a2f24 35%, #2b1a17 70%); }
  .hero-title { position: absolute; left: 57px; top: 138px; font-size: 32px; color: #fff; font-weight: 400; }
  .hero-sub { position: absolute; left: 57px; top: 183px; font-size: 16px; color: #fff; }
  .hero-dots { position: absolute; left: 363px; top: 358px; display: flex; gap: 3px; }
  .hero-dots span { width: 9px; height: 9px; border-radius: 50%; background: #9a9a9a; }
  .hero-dots span:first-child { background: #fff; }

  .welcome { position: absolute; left: 124px; top: 516px; width: 771px; text-align: center; }
  .welcome h1 { font-size: 27px; font-weight: 400; color: var(--ink); }
  .welcome p { margin: 10px auto 0; width: 760px; font-family: "Questrial", sans-serif; font-size: 10.4px; line-height: 16.5px; color: var(--muted); }

  .service { position: absolute; top: 647px; width: 246px; }
  .service-image { width: 246px; height: 107px; border: 1px solid #e2e2e2; padding: 4px; background: #fff; box-shadow: 0 1px 2px rgba(0,0,0,0.08); }
  .service-image div { width: 100%; height: 100%; }
  .service h2 { margin-top: 15px; font-size: 16px; font-weight: 400; color: var(--blue); padding-left: 2px; }
  .service p { margin-top: 6px; font-size: 9.6px; line-height: 15px; color: var(--muted); padding-left: 2px; }
  .service a { display: block; margin-top: 4px; font-size: 11.5px; color: var(--red); text-decoration: none; padding-left: 2px; }

  .divider { position: absolute; left: 124px; top: 875px; width: 766px; height: 1px; background: var(--rule); }

  .blog { position: absolute; left: 123px; top: 910px; width: 350px; }
  .blog h2 { font-size: 22px; font-weight: 400; color: var(--red); }
  .blog h3 { margin-top: 12px; font-size: 13px; font-weight: 400; color: var(--ink); }
  .blog p { margin-top: 5px; font-size: 9.9px; line-height: 15.2px; color: var(--muted); }
  .blog a { display: block; margin-top: 7px; font-size: 12px; font-weight: 700; color: var(--blue); text-decoration: none; letter-spacing: 0.3px; }

  .about { position: absolute; left: 497px; top: 910px; width: 395px; }
  .about h2 { font-size: 22px; font-weight: 400; color: var(--blue); }
  .about-photo { position: absolute; left: 0; top: 38px; width: 116px; height: 95px; border-radius: 3px;
    background: linear-gradient(135deg, #e4ecf3 0%, #b9cbdc 55%, #6d87a6 100%); }
  .about-lead { position: absolute; left: 129px; top: 38px; width: 266px; font-size: 11.6px; line-height: 15.5px; color: var(--muted); }
  .about-body { position: absolute; left: 129px; top: 75px; width: 266px; font-size: 9.7px; line-height: 15.2px; color: var(--muted); }

  .site-footer { position: absolute; left: 0; top: 1107px; width: 1019px; height: 93px; background: var(--footer); border-top: 1px solid #ececec; }
  .footer-nav { position: absolute; left: 126px; top: 27px; font-size: 13px; color: var(--ink); }
  .footer-nav a { color: var(--ink); text-decoration: none; }
  .footer-nav span { margin: 0 5px; }
  .copyright { position: absolute; left: 126px; top: 52px; font-size: 9.5px; color: #999; }
  .social { position: absolute; left: 822px; top: 30px; display: flex; gap: 6px; }
  .social span { width: 18px; height: 18px; border-radius: 2px; }
  .social .one { background: #3b5a9a; }
  .social .two { background: #4cb6e8; }
  .social .three { background: #1b75b0; }
</style>
</head>
<body>
  <div class="header-band"></div>
  <div class="cream-band"></div>

  <div class="brand">R. MORVANE</div>

  <nav class="main-nav">
    <a href="#">About Us</a>
    <a href="#">Our Services</a>
    <a href="#">Blog</a>
    <a href="#">Testimonials</a>
    <a href="#">Contact</a>
  </nav>

  <section class="hero">
    <div class="hero-photo" role="img" aria-label="Portrait photo of the consultant in a dark blazer, arms crossed, smiling"></div>
    <h2 class="hero-title">PhD. in Counseling Psychology</h2>
    <p class="hero-sub">MBA in Human Development &amp; Family Studies</p>
    <div class="hero-dots"><span></span><span></span><span></span><span></span></div>
  </section>

  <section class="welcome">
    <h1>Welcome to My Website Maipage</h1>
    <p>Mauris vel lacus vitae felis vestibulum volutpat Etiam est nunc venenatis in tristique eu imperdiet ac nisl Cum sociis natoque penatibus et magnis dis parturient montes nascetur ridiculus mus In iaculis facilisis massa Etiam eu urna Sed porta Suspendisse quam leo molestie sed luctus quis feugiat in pede Fusce tellus Sed metus augue convallis et vehicula ut pulvinar eu ante Integer orci tellus tristique vitae</p>
  </section>

  <article class="service" style="left:124px">
    <div class="service-image"><div role="img" aria-label="Photo of an empty lecture hall with blue seats seen from behind a podium" style="background:linear-gradient(180deg,#cfe0ea 0%,#3f6fae 55%,#a7443a 85%,#d8a53c 100%)"></div></div>
    <h2>Keynote Speaker</h2>
    <p>Etiam est nunc venenatis in tristique eu imperdiet ac nisl<br>Cum sociis natoque penatibus et magnis dis</p>
    <a href="#">Read More</a>
  </article>

  <article class="service" style="left:387px">
    <div class="service-image"><div role="img" aria-label="Photo of business people shaking hands in an office" style="background:linear-gradient(90deg,#6f7c8c 0%,#d8dde2 45%,#9aa6b1 70%,#e9ecef 100%)"></div></div>
    <h2>Executive Coach</h2>
    <p>Etiam est nunc venenatis in tristique eu imperdiet ac nisl<br>Cum sociis natoque penatibus et magnis dis</p>
    <a href="#">Read More</a>
  </article>

  <article class="service" style="left:649px">
    <div class="service-image"><div role="img" aria-label="Photo of a woman joining a video conference shown on a monitor" style="background:linear-gradient(90deg,#2a2a2a 0%,#cfd3d6 35%,#e6e7e8 60%,#5a4438 100%)"></div></div>
    <h2>Webinar Training Instructor</h2>
    <p>Etiam est nunc venenatis in tristique eu imperdiet ac nisl<br>Cum sociis natoque penatibus et magnis dis</p>
    <a href="#">Read More</a>
  </article>

  <div class="divider"></div>

  <section class="blog">
    <h2>Recent Blog Post</h2>
    <h3>Enatis in tristique eu imperdiet ac nisl</h3>
    <p>ro lectus feugiat felis Morbi diam mauris viverra in gravida eu mattis in ante Morbi eget arcu Morbi porta libero id ullamcorper nonummy nibh ligula pulvinar metus eget consectetuer augue nisi quis lacus</p>
    <a href="#">VIEW ALL</a>
  </section>

  <section class="about">
    <h2>Little About Me</h2>
    <div class="about-photo" role="img" aria-label="Photo of a smiling team of professionals standing together"></div>
    <p class="about-lead">Eifend libero a tempus libero lectus feugiat felis Morbi diam mauris viverra in gravida</p>
    <p class="about-body">Morbi eget arcu Morbi porta libero id ullamcorper nonummy nibh ligula pulvinar metus eget consectetuer augue nisi quis lacus Ut ac mi quis lacus mollis aliquam Curabitur iaculis tempus eros Curabitur vel mi sit amet magna</p>
  </section>

  <footer class="site-footer">
    <nav class="footer-nav">
      <a href="#">About Us</a><span>|</span><a href="#">Our Services</a><span>|</span><a href="#">Blog</a><span>|</span><a href="#">Testimonials</a><span>|</span><a href="#">Contact</a>
    </nav>
    <p class="copyright">© 2014 Company Name &nbsp;All right reserved &nbsp;Term of Use</p>
    <div class="social">
      <span class="one" role="img" aria-label="Social profile link"></span>
      <span class="two" role="img" aria-label="Social profile link"></span>
      <span class="three" role="img" aria-label="Social profile link"></span>
    </div>
  </footer>
</body>
</html>
```